Start up in business consultancy needs a business card

We need the business card's layout (we have already the logo). Our business is concerned on consultancy services delivered to companies on the matter of sustainability. Business card should be enough essentials and professional style.

Side A with the following info:
logo + a space for the claim (still to identify) + website of the company

Side B with the following info:
Name of business card holder + title of the business card holder + address of the company + space for mobile number, phone number, fax number + e-mail of business card holder + graphic details around.

Target Market(s)

Business of any sector

Industry/Entity Type

Business Service

Contact Information for Business Card

Name of the company:
Lumeroca srl
Società Benefit

Address of the company:
Via Pescoli, 7
21099 - Castelvarno (CV)

Website:
www.lumeroca-esempio.it

Name of the BC' holder:
Ettore Valsenzi

Title:
Co-fondatore

Email:
ettore@lumeroca-esempio.it

Mobile:
+39 351 602 7415
Phone:
+39 351 602 7415
Fax:
+39 351 602 7415

Font styles to use
Other font styles liked:
• new gothic

```html
<!DOCTYPE html>
<html lang="it">
<head>
<meta charset="utf-8">
<title>Lumeroca – biglietto da visita</title>
<link href="https://fonts.googleapis.com/css2?family=Questrial&family=Rubik:wght@400;700&display=swap" rel="stylesheet">
<style>
  :root {
    --bg: #a3a1a1;
    --paper: #f5f5f5;
    --brand-blue: #0e6aa9;
    --ink: #333333;
    --ink-soft: #3c3c3c;
    --curve-shade: #3d4043;
    --faint: #e6e6e6;
  }
  * { margin: 0; padding: 0; box-sizing: border-box; }
  html, body { width: 1200px; height: 1200px; overflow: hidden; }
  body { background: var(--bg); position: relative; font-family: "Questrial", sans-serif; color: var(--ink); }

  .card { position: absolute; width: 712px; height: 418px; background: var(--paper); overflow: hidden; }
  .card--front { left: 238px; top: 118px; }
  .card--back { left: 231px; top: 644px; }

  /* front */
  .front-deco { position: absolute; left: 400px; top: 30px; }
  .brand { position: absolute; left: 137px; top: 133px; display: flex; align-items: center; gap: 22px; }
  .brand__dot { width: 132px; height: 132px; border: 4px solid var(--brand-blue); border-radius: 50%; }
  .brand__name { font-family: "Questrial", sans-serif; font-size: 50px; color: var(--brand-blue); letter-spacing: 1.5px; }
  .front-web { position: absolute; left: 0; right: 0; top: 374px; display: flex; justify-content: center; align-items: center; gap: 18px; }
  .front-web__rule { width: 62px; height: 2px; background: var(--brand-blue); }
  .front-web__url { font-size: 20px; color: var(--ink-soft); letter-spacing: 0.8px; }

  /* back */
  .back-panel { position: absolute; inset: 0; }
  .back-brand { position: absolute; left: 0; width: 290px; top: 122px; display: flex; flex-direction: column; align-items: center; gap: 20px; }
  .back-brand__dot { width: 128px; height: 128px; border: 4px solid #ffffff; border-radius: 50%; }
  .back-brand__name { font-size: 36px; color: #ffffff; letter-spacing: 0.5px; }

  .holder { position: absolute; right: 25px; top: 46px; text-align: right; }
  .holder__name { font-family: "Rubik", sans-serif; font-weight: 700; font-size: 26px; color: var(--ink); }
  .holder__title { font-family: "Rubik", sans-serif; font-size: 15px; color: var(--ink); margin-top: 6px; }

  .company { position: absolute; right: 25px; top: 218px; font-size: 22px; color: var(--ink-soft); letter-spacing: 1px; }
  .contacts { position: absolute; right: 25px; top: 252px; list-style: none; text-align: right; }
  .contacts li { font-size: 17.5px; line-height: 22.3px; color: var(--ink-soft); letter-spacing: 0.4px; display: flex; justify-content: flex-end; align-items: center; gap: 8px; }
  .contacts svg { width: 15px; height: 15px; fill: var(--brand-blue); }
  .address { position: absolute; right: 25px; top: 368px; font-size: 18px; color: var(--ink-soft); letter-spacing: 0.4px; }
</style>
</head>
<body>

<section class="card card--front">
  <svg class="front-deco" width="380" height="360" viewBox="0 0 380 360" aria-hidden="true">
    <circle cx="170" cy="180" r="170" fill="none" stroke="var(--faint)" stroke-width="10"/>
  </svg>
  <div class="brand">
    <span class="brand__dot"></span>
    <span class="brand__name">lumeroca</span>
  </div>
  <div class="front-web">
    <span class="front-web__rule"></span>
    <span class="front-web__url">www.lumeroca-esempio.it</span>
    <span class="front-web__rule"></span>
  </div>
</section>

<section class="card card--back">
  <svg class="back-panel" width="712" height="418" viewBox="0 0 712 418" aria-hidden="true">
    <path d="M0 0 H286 C302 60 322 140 320 250 C318 330 302 385 280 418 H0 Z" fill="var(--curve-shade)"/>
    <path d="M0 0 H284 C300 60 318 140 314 250 C311 330 295 380 268 418 H0 Z" fill="var(--brand-blue)"/>
  </svg>
  <div class="back-brand">
    <span class="back-brand__dot"></span>
    <span class="back-brand__name">lumeroca</span>
  </div>

  <div class="holder">
    <div class="holder__name">Ettore Valsenzi</div>
    <div class="holder__title">Co-fondatore</div>
  </div>

  <div class="company">Lumeroca srl Società Benefit</div>
  <ul class="contacts">
    <li>+39 351 602 7415 <svg viewBox="0 0 16 16"><path d="M4 0h8a1 1 0 0 1 1 1v14a1 1 0 0 1-1 1H4a1 1 0 0 1-1-1V1a1 1 0 0 1 1-1zm1 2v10h6V2z"/></svg></li>
    <li>+39 351 602 7415 <svg viewBox="0 0 16 16"><path d="M1 6c0-3 14-3 14 0v2h-4V6H5v2H1zM3 9l2-2h6l2 2v6H3z"/></svg></li>
    <li>+39 351 602 7415 <svg viewBox="0 0 16 16"><path d="M4 1h8v4H4zM1 6h14v6h-3v3H4v-3H1zm4 4v4h6v-4z"/></svg></li>
    <li>ettore@lumeroca-esempio.it <svg viewBox="0 0 16 16"><path d="M0 3h16v10H0zm1.5 1.2L8 9l6.5-4.8V4h-13z"/></svg></li>
    <li>www.lumeroca-esempio.it <svg viewBox="0 0 16 16"><path d="M8 0a8 8 0 1 0 0 16A8 8 0 0 0 8 0zm-1 1.6V5H4.3A6.5 6.5 0 0 1 7 1.6zm2 0A6.5 6.5 0 0 1 11.7 5H9zM1.6 7H7v2H1.6a6 6 0 0 1 0-2zM9 7h5.4a6 6 0 0 1 0 2H9zm-4.7 4H7v3.4A6.5 6.5 0 0 1 4.3 11zM9 11h2.7A6.5 6.5 0 0 1 9 14.4z"/></svg></li>
  </ul>
  <div class="address">Via Pescoli, 7 21099 - Castelvarno (CV)</div>
</section>

</body>
</html>
```